Meridel Nutrition needs Stationary and a business card

We would like to use our current logo. The text can be moved around as needed. The stationary needs to be a 'first page' where the logo is more prominent to be impressive on higher quality paper and a second page where the logo is more subtle where there will be much more information on the page. There are 2 clinic locations which will need include name, address, phone number, fax number, web address. The business card should be single sided and contain this information also.
The design must be contemporary and sophisticated as this is a science based diet run out of a medical clinic.

Target Market(s)

People wanting to lose weight, athletes looking to optimise performance, people with arthritis or fighting cancer

Industry/Entity Type

Business

Contact Information for Business Card

must use the logo. I have attached an example card with the practice details on it. there must be space for the doctors name. Also the website www.meridelnutrition.com.au

Requirements
Must have
• the logo, the business adresses and phone numbers, the website, the doctors name and qualifications
Nice to have
• some creativity
Should not have
• Do not simply reproduce the existing card please

```html
<!DOCTYPE html>
<html lang="en">
<head>
<meta charset="utf-8">
<title>Meridel Nutrition Stationery</title>
<link href="https://fonts.googleapis.com/css2?family=Didact+Gothic&display=swap" rel="stylesheet">
<style>
:root{
  --navy:#44628f;
  --sky:#63b6ec;
  --paper:#f5f5f5;
  --ink:#3b3f48;
  --backdrop:#d2d2d4;
}
*{box-sizing:border-box;margin:0;padding:0}
html,body{width:1200px;height:991px;overflow:hidden}
body{background:var(--backdrop);font-family:"Didact Gothic",sans-serif;color:var(--ink);position:relative}
.sheet{position:absolute;background:var(--paper);overflow:hidden}
.band{position:absolute;left:0;bottom:0;width:100%}
.band svg{display:block;width:100%;height:100%}
.brand{position:absolute;display:flex;flex-direction:column;align-items:center;transform:translateX(-50%)}
.brand-dot{border-radius:50%;background:var(--sky)}
.brand-name{color:var(--navy);letter-spacing:.02em;white-space:nowrap;text-transform:uppercase}

/* letterhead */
.letterhead{left:71px;top:103px;width:397px;height:561px}
.letterhead .brand{left:50%;top:32px}
.letterhead .brand-dot{width:46px;height:46px;margin-bottom:6px}
.letterhead .brand-name{font-size:9px}
.letter{position:absolute;left:26px;right:25px;top:208px;font-size:6.3px;line-height:7.2px;text-align:justify}
.letter p{margin-bottom:7px}
.letter .salute,.letter .signer{font-weight:bold;color:#222}
.signature{position:absolute;left:70px;bottom:-28px;width:86px;height:30px;background:linear-gradient(90deg,rgba(80,96,170,.08),rgba(80,96,170,.2),rgba(80,96,170,.06));border-radius:12px}
.closing{position:relative;margin-top:12px}
.letterhead .band{height:46px}
.footer{position:absolute;left:26px;right:25px;bottom:9px;display:flex;justify-content:space-between;color:#e6edf6;font-size:5.2px;line-height:1.3}
.footer .right{text-align:right}
.footer b{color:#fff;letter-spacing:.03em}

/* folder */
.folder{left:507px;top:90px;width:432px;height:576px}
.folder .spine{position:absolute;left:26px;top:0;width:1px;height:248px;background:#e2e2e2}
.folder .brand{left:54%;top:65px}
.folder .brand-dot{width:78px;height:78px;margin-bottom:10px}
.folder .brand-name{font-size:14px}
.folder .band{height:330px}
.folder .site{position:absolute;left:0;right:0;bottom:36px;text-align:center;color:#d6e0ee;font-size:7.5px;letter-spacing:.04em}

/* business card front */
.card-front{left:66px;top:696px;width:170px;height:95px}
.card-front .col{position:absolute;top:10px;font-size:3.9px;line-height:1.25;color:#555}
.card-front .col b{color:var(--navy)}
.card-front .left{left:10px}
.card-front .right{right:10px;text-align:right}
.card-front .brand{left:50%;top:11px}
.card-front .brand-dot{width:29px;height:29px;margin-bottom:4px}
.card-front .brand-name{font-size:6px}
.card-front .band{height:37px}
.card-front .doctor{position:absolute;left:0;right:0;bottom:9px;text-align:center;color:#d8e2ef;font-size:3.9px;line-height:1.3}
.card-front .doctor b{color:var(--sky);font-size:4.6px}

/* business card back */
.card-back{left:66px;top:810px;width:170px;height:95px;background:var(--navy)}
.card-back .brand{left:50%;top:24px}
.card-back .brand-dot{width:31px;height:31px;margin-bottom:5px}
.card-back .brand-name{font-size:6.5px;color:#fff}

/* compliment slip */
.slip{left:266px;top:696px;width:415px;height:208px}
.slip .brand{left:57px;top:20px;transform:none}
.slip .brand-dot{width:46px;height:46px;margin-bottom:6px}
.slip .brand-name{font-size:8.6px}
.slip .address{font-size:5.2px;line-height:1.3;text-align:center;margin-top:5px;color:#555}
.slip .band{height:28px}

/* envelope */
.envelope{left:718px;top:696px;width:415px;height:208px}
.envelope .flap{position:absolute;left:0;top:0;width:100%;height:60px}
.envelope .flap svg{width:100%;height:100%;display:block}
.envelope .seal{position:absolute;left:50%;top:17px;transform:translateX(-50%);width:24px;height:24px;border-radius:50%;background:var(--sky)}
.envelope .site{position:absolute;left:0;right:0;bottom:20px;text-align:center;font-size:5.2px;color:#555}
</style>
</head>
<body>

<section class="sheet letterhead">
  <div class="brand"><span class="brand-dot"></span><span class="brand-name">Meridel Nutrition</span></div>
  <div class="letter">
    <p class="salute">Dear sir,</p>
    <p>Communication is a very integral part of living creatures, animals and humans. Communication may be verbal or written. Written communication however is only applicable to human beings. Can you even imagine a world without communication? Verbal communication can be through telephones, webcams or in person. Written communication is through letters, emails and mobile phone messages.</p>
    <p>In today's world of great inventions and technology, letters have somehow become redundant. It is the time for text messages or chats. But they still can communicate a lot more than all other modes of communication. Organizations and various government departments still bank on letters as a strong medium of communication. There is no comparison in costs of sending letters as compared to costs of mobile phone messages though – letters are far cheaper. Letters now commonly known as "hard copy documents" are considered more relevant and important than email copies of text messages as proof or evidence of some sort.</p>
    <p>Letters speak volumes about a person or an organization that writes it. So one must take utmost care ensuring that the language used in any letter is appropriate for the occasion for which it is being written. Since a letter is also a written proof or document, if there are certain things that should not form a part of it, then that too should be carefully handled.</p>
    <p>Writing a good letter is an art. But if for some reason someone is unable to write that perfect letter, these different types of letters provide a base for you to build on. Sample letters have been given for everyone to understand what all information needs to form a part of the letter type and then it can be customized.</p>
    <div class="closing">Yours Sincerely,<br><span class="signer">Clara Venn</span>
      <span class="signature" role="img" aria-label="Handwritten signature"></span>
    </div>
  </div>
  <div class="band">
    <svg viewBox="0 0 400 100" preserveAspectRatio="none" aria-hidden="true">
      <path d="M0 0 Q200 26 400 0 L400 100 L0 100Z" fill="var(--sky)"/>
      <path d="M0 6 Q200 40 400 6 L400 100 L0 100Z" fill="var(--navy)"/>
    </svg>
  </div>
  <div class="footer">
    <div><b>ASHGROVE</b><br>12-14 Linden Street, Ashgrove 2140 NSW<br>Phone (02) 9000 4812 · www.meridelnutrition.com.au</div>
    <div class="right"><b>WESTVALE</b><br>88 Carrow Road, Westvale 2035 NSW<br>Phone (02) 9000 7395 · www.harbourjointclinic.com.au</div>
  </div>
</section>

<section class="sheet folder">
  <span class="spine"></span>
  <div class="brand"><span class="brand-dot"></span><span class="brand-name">Meridel Nutrition</span></div>
  <div class="band">
    <svg viewBox="0 0 400 330" preserveAspectRatio="none" aria-hidden="true">
      <path d="M0 0 Q200 22 400 0 L400 330 L0 330Z" fill="var(--sky)"/>
      <path d="M0 4 Q200 34 400 4 L400 330 L0 330Z" fill="var(--navy)"/>
    </svg>
  </div>
  <div class="site">www.meridelnutrition.com.au</div>
</section>

<section class="sheet card-front">
  <div class="col left"><b>Ashgrove</b><br>12-14 Linden Street<br>Ashgrove 2140 NSW<br>Phone (02) 9000 4812<br>meridelnutrition.com.au</div>
  <div class="col right"><b>Westvale</b><br>88 Carrow Road<br>Westvale 2035 NSW<br>Phone (02) 9000 7395<br>harbourjointclinic.com.au</div>
  <div class="brand"><span class="brand-dot"></span><span class="brand-name">Meridel Nutrition</span></div>
  <div class="band">
    <svg viewBox="0 0 400 100" preserveAspectRatio="none" aria-hidden="true">
      <path d="M0 0 Q200 22 400 0 L400 100 L0 100Z" fill="var(--sky)"/>
      <path d="M0 6 Q200 34 400 6 L400 100 L0 100Z" fill="var(--navy)"/>
    </svg>
  </div>
  <div class="doctor"><b>Dr ELIAS VARN</b><br>MBBS BMedSc FRACP<br>Clinical Nutrition Physician</div>
</section>

<section class="sheet card-back">
  <div class="brand"><span class="brand-dot"></span><span class="brand-name">Meridel Nutrition</span></div>
</section>

<section class="sheet slip">
  <div class="brand">
    <span class="brand-dot"></span><span class="brand-name">Meridel Nutrition</span>
    <div class="address">12-14 Linden Street<br>Ashgrove 2140 NSW</div>
  </div>
  <div class="band">
    <svg viewBox="0 0 400 100" preserveAspectRatio="none" aria-hidden="true">
      <path d="M0 0 Q200 32 400 0 L400 100 L0 100Z" fill="var(--sky)"/>
      <path d="M0 10 Q200 48 400 10 L400 100 L0 100Z" fill="var(--navy)"/>
    </svg>
  </div>
</section>

<section class="sheet envelope">
  <div class="flap">
    <svg viewBox="0 0 415 60" preserveAspectRatio="none" aria-hidden="true">
      <path d="M0 0 H415 L403 49 Q401 58 392 58 H23 Q14 58 12 49 Z" fill="var(--navy)"/>
    </svg>
  </div>
  <span class="seal"></span>
  <div class="site">www.meridelnutrition.com.au</div>
</section>

</body>
</html>
```